Search Fund needs a PowerPoint template design

We need a eye-catching and compelling PowerPoint design for a new company based in Chicago called Tarn Ridge Partners. We are search fund with a primary mission to acquire a founder/family/entrepreneur owned businesses (This is similar to a Private Equity firm). Our goal is to offer investors a unique avenue to invest in an attractive business acquisition while providing business owners with an alternative path to exit. We would like the design to reflect crisp and professional nature that many financial firms present. The template should build on the design of the logo including expanding a logical color palette. The presentation will be used to describe facts regarding the firm, financial data and key messaging that we want our investors and potential partners to takeaway.

Target Market(s)

Financial Investors

Industry/Entity Type

Finance

Font styles to use
Serif
Sans Serif

Colors

Designer to choose colors to be used in the design.

Requirements
Must have
• Should include cover page and slide examples. Attractive data displays (graphs, charts, infographics etc.); Compelling cover; fly pages to put in between sections; table of contents page. Needs to have white space to add text.
Should not have
• Do not redesign the logo or change the logo colors. Additional colors should be added to the PowerPoint template

```html
<!DOCTYPE html>
<html lang="en">
<head>
<meta charset="utf-8">
<title>Tarn Ridge Partners – Presentation Template</title>
<link href="https://fonts.googleapis.com/css2?family=Open+Sans:wght@400;600;700&display=swap" rel="stylesheet">
<style>
:root{
  --board:#ececec;
  --ink:#222;
  --brand-blue:#1a6fc0;
  --text-blue:#2467b8;
  --grey-dark:#3d3d3d;
  --grey-mid:#9a9a9a;
  --grey-text:#555;
  --green:#8cc21e;
  --green-dark:#3f8a12;
  --white:#fff;
}
*{margin:0;padding:0;box-sizing:border-box}
html,body{width:1200px;height:1200px;overflow:hidden;background:var(--board);font-family:"Open Sans",Arial,sans-serif;color:var(--ink)}
.board{position:relative;width:1200px;height:1200px}
.label{position:absolute;width:560px;text-align:center;font-size:22px;font-weight:400;color:var(--ink)}
.slide-frame{position:absolute;width:560px;height:316px}
.slide{position:absolute;left:0;top:0;width:700px;height:395px;transform:scale(.8);transform-origin:0 0;background:var(--white);overflow:hidden;box-shadow:0 4px 10px rgba(0,0,0,.35)}
.slide svg.decor{position:absolute;left:0;top:0}
.header{position:absolute;left:0;top:0;width:700px;height:70px;background:var(--white);box-shadow:0 3px 6px rgba(0,0,0,.15)}
.wordmark{position:absolute;top:22px;font-weight:700;font-size:21px;letter-spacing:1px;color:var(--brand-blue);white-space:nowrap;text-transform:uppercase}
.title{position:absolute;font-size:28px;font-weight:400;text-transform:uppercase;white-space:nowrap}
.title.grey{color:var(--grey-text)}
.title.blue{color:var(--text-blue)}
.subtitle{position:absolute;font-size:14.5px;color:var(--text-blue)}
.bullets{position:absolute;font-size:12.5px;line-height:16px;color:var(--grey-text);list-style:none}
.bullets li{position:relative;padding-left:16px;margin-bottom:7px}
.bullets li::before{content:"•";position:absolute;left:0;top:0}
.para{position:absolute;font-size:12.5px;line-height:16px;color:var(--text-blue)}
.footer{position:absolute;top:378px;font-size:7px;color:var(--grey-text)}
.page-num{position:absolute;top:378px;font-size:7px;color:var(--grey-text)}
.cover{background:var(--grey-mid)}
.cover-band{position:absolute;left:0;top:139px;width:700px;height:119px;background:var(--white);box-shadow:0 3px 8px rgba(0,0,0,.3)}
.cover .wordmark{top:40px;left:0;width:700px;text-align:center;font-size:36px;letter-spacing:2px}
.toc-panel{position:absolute;left:0;top:70px;width:700px;height:325px;background:var(--grey-mid)}
.toc-title{position:absolute;left:245px;top:102px;font-size:30px;color:var(--white)}
.toc{position:absolute;left:245px;top:164px;width:235px;list-style:none;font-size:12.5px;color:var(--white)}
.toc li{display:flex;height:34px}
.toc .dots{flex:1;border-bottom:1px dotted var(--white);margin:0 2px 19px}
</style>
</head>
<body>
<div class="board">

  <!-- Cover -->
  <div class="label" style="left:36px;top:26px">Cover</div>
  <div class="slide-frame" style="left:36px;top:62px">
    <div class="slide cover">
      <svg class="decor" width="700" height="395" role="img" aria-label="Layered green, white and charcoal triangle composition">
        <defs>
          <linearGradient id="coverArt" x1="0" y1="0" x2="1" y2="1">
            <stop offset="0" stop-color="#8f8f8f"/>
            <stop offset=".35" stop-color="#6aa51c"/>
            <stop offset=".6" stop-color="#d9d9d9"/>
            <stop offset="1" stop-color="#4a4a4a"/>
          </linearGradient>
        </defs>
        <rect x="70" y="0" width="600" height="395" fill="url(#coverArt)" opacity=".75"/>
      </svg>
      <div class="cover-band"><div class="wordmark">Tarn Ridge Partners</div></div>
    </div>
  </div>

  <!-- Headline with subheadline and bullet -->
  <div class="label" style="left:615px;top:26px">Headline with subheadline and bullet</div>
  <div class="slide-frame" style="left:615px;top:62px">
    <div class="slide">
      <svg class="decor" width="700" height="395" role="img" aria-label="Green diagonal panel with layered triangle composition">
        <defs>
          <linearGradient id="sideArtA" x1="0" y1="0" x2="0" y2="1">
            <stop offset="0" stop-color="#6f6f6f"/>
            <stop offset=".5" stop-color="#5aa01a"/>
            <stop offset="1" stop-color="#8cc21e"/>
          </linearGradient>
        </defs>
        <polygon points="0,0 182,0 0,362" fill="url(#sideArtA)"/>
      </svg>
      <div class="header"><div class="wordmark" style="left:0;width:700px;text-align:center;padding-left:0">Tarn Ridge Partners</div></div>
      <div class="title grey" style="left:148px;top:100px">Key Messaging</div>
      <div class="subtitle" style="left:148px;top:151px">Our investors and potential partners</div>
      <ul class="bullets" style="left:148px;top:190px;width:510px">
        <li>Our goal is to offer investors a unique avenue to invest in an attractive business acquisition while providing business owners with an alternative path to exit.</li>
        <li>We would like the design to reflect crisp and professional nature that many financial firms present.</li>
        <li>The template should build on the design of the logo including expanding a logical color palette.</li>
      </ul>
      <div class="footer" style="left:333px">TARN RIDGE ©2019</div>
      <div class="page-num" style="left:653px">5</div>
    </div>
  </div>

  <!-- Content -->
  <div class="label" style="left:40px;top:419px">Content</div>
  <div class="slide-frame" style="left:40px;top:453px">
    <div class="slide">
      <div class="toc-panel"></div>
      <svg class="decor" width="700" height="395" role="img" aria-label="Green diagonal panel with layered triangle composition">
        <defs>
          <linearGradient id="sideArtB" x1="0" y1="0" x2="0" y2="1">
            <stop offset="0" stop-color="#8cc21e"/>
            <stop offset=".45" stop-color="#505050"/>
            <stop offset="1" stop-color="#8cc21e"/>
          </linearGradient>
        </defs>
        <polygon points="0,0 120,0 215,395 0,395" fill="url(#sideArtB)"/>
      </svg>
      <div class="header"><div class="wordmark" style="left:0;width:700px;text-align:center">Tarn Ridge Partners</div></div>
      <div class="toc-title">Content</div>
      <ul class="toc">
        <li><span>Primary mission</span><span class="dots"></span><span>3</span></li>
        <li><span>Financial data</span><span class="dots"></span><span>4</span></li>
        <li><span>Key messaging</span><span class="dots"></span><span>5</span></li>
        <li><span>Investors</span><span class="dots"></span><span>5</span></li>
        <li><span>Potential partners</span><span class="dots"></span><span>6</span></li>
      </ul>
    </div>
  </div>

  <!-- Headline and bullet -->
  <div class="label" style="left:615px;top:416px">Headline and bullet</div>
  <div class="slide-frame" style="left:615px;top:453px">
    <div class="slide">
      <svg class="decor" width="700" height="395" role="img" aria-label="Green diagonal panel with layered triangle composition">
        <defs>
          <linearGradient id="sideArtC" x1="0" y1="0" x2="0" y2="1">
            <stop offset="0" stop-color="#4a4a4a"/>
            <stop offset=".4" stop-color="#4f9a16"/>
            <stop offset="1" stop-color="#8cc21e"/>
          </linearGradient>
        </defs>
        <polygon points="0,0 30,0 126,395 0,395" fill="url(#sideArtC)"/>
      </svg>
      <div class="header"><div class="wordmark" style="left:0;width:700px;text-align:center">Tarn Ridge Partners</div></div>
      <div class="title blue" style="left:168px;top:96px">Financial Data</div>
      <ul class="bullets" style="left:168px;top:151px;width:470px">
        <li>Our goal is to offer investors a unique avenue to invest in an attractive business acquisition while providing business owners with an alternative path to exit.</li>
        <li>We would like the design to reflect crisp and professional nature that many financial firms present.</li>
        <li>The template should build on the design of the logo including expanding a logical color palette.</li>
        <li>The presentation will be used to describe facts regarding the firm, financial data and key messaging that we want our investors and potential partners to takeaway.</li>
      </ul>
      <div class="footer" style="left:333px">TARN RIDGE ©2019</div>
      <div class="page-num" style="left:653px">4</div>
    </div>
  </div>

  <!-- Headline -->
  <div class="label" style="left:37px;top:795px">Headline</div>
  <div class="slide-frame" style="left:37px;top:831px">
    <div class="slide">
      <svg class="decor" width="700" height="395" role="img" aria-label="Green diagonal panel with layered triangle composition">
        <defs>
          <linearGradient id="sideArtD" x1="0" y1="0" x2="0" y2="1">
            <stop offset="0" stop-color="#d9d9d9"/>
            <stop offset=".4" stop-color="#4a4a4a"/>
            <stop offset=".7" stop-color="#4f9a16"/>
            <stop offset="1" stop-color="#8cc21e"/>
          </linearGradient>
        </defs>
        <polygon points="560,0 700,0 700,395 490,395 560,120" fill="url(#sideArtD)"/>
      </svg>
      <div class="header"><div class="wordmark" style="left:0;width:700px;text-align:center">Tarn Ridge Partners</div></div>
      <div class="title grey" style="left:29px;top:100px">Primary Mission</div>
      <p class="para" style="left:29px;top:166px;width:450px">Our goal is to offer investors a unique avenue to invest in an attractive business acquisition while providing business owners with an alternative path to exit. We would like the design to reflect crisp and professional nature that many financial firms present. The template should build on the design of the logo including expanding a logical color palette.</p>
      <p class="para" style="left:29px;top:276px;width:450px">The presentation will be used to describe facts regarding the firm, financial data and key messaging that we want our investors and potential partners to takeaway.</p>
      <div class="footer" style="left:333px">TARN RIDGE ©2019</div>
    </div>
  </div>

  <!-- Headline and image -->
  <div class="label" style="left:615px;top:794px">Headline and image</div>
  <div class="slide-frame" style="left:615px;top:831px">
    <div class="slide">
      <svg class="decor" width="700" height="395" role="img" aria-label="Green diagonal panel with layered triangle composition">
        <defs>
          <linearGradient id="sideArtE" x1="0" y1="0" x2="0" y2="1">
            <stop offset="0" stop-color="#8cc21e"/>
            <stop offset=".45" stop-color="#4a4a4a"/>
            <stop offset=".75" stop-color="#4f9a16"/>
            <stop offset="1" stop-color="#8cc21e"/>
          </linearGradient>
        </defs>
        <polygon points="520,0 700,0 700,395 640,395 545,200" fill="url(#sideArtE)"/>
      </svg>
      <div class="header"><div class="wordmark" style="left:0;width:700px;text-align:center">Tarn Ridge Partners</div></div>
      <div class="title blue" style="left:149px;top:96px">Potential Partners</div>
      <svg class="chart-pie" style="position:absolute;left:0;top:0" width="270" height="320" viewBox="0 0 270 320">
        <path d="M26 208 A110 46 0 0 0 246 208 L246 236 A110 46 0 0 1 26 236 Z" fill="#b98a00"/>
        <g transform="translate(136 208) scale(1 .42)">
          <path d="M0 0 L0 -110 A110 110 0 0 1 55 -95.3 Z" fill="#3a6fcc"/>
          <path d="M0 0 L55 -95.3 A110 110 0 0 1 108.3 19.1 Z" fill="#e87f2a"/>
          <path d="M0 0 L108.3 19.1 A110 110 0 0 1 -103.4 37.6 Z" fill="#f7be00"/>
          <path d="M0 0 L-103.4 37.6 A110 110 0 0 1 -95.3 -55 Z" fill="#5a9ad8"/>
          <path d="M0 0 L-95.3 -55 A110 110 0 0 1 0 -110 Z" fill="#6aab3a"/>
        </g>
        <g font-size="5" fill="#555">
          <circle cx="103" cy="313" r="1.5" fill="#3a6fcc"/><text x="106" y="315">1</text>
          <circle cx="114" cy="313" r="1.5" fill="#e87f2a"/><text x="117" y="315">2</text>
          <circle cx="125" cy="313" r="1.5" fill="#9a9a9a"/><text x="128" y="315">3</text>
          <circle cx="136" cy="313" r="1.5" fill="#f7be00"/><text x="139" y="315">4</text>
          <circle cx="147" cy="313" r="1.5" fill="#5a9ad8"/><text x="150" y="315">5</text>
          <circle cx="158" cy="313" r="1.5" fill="#6aab3a"/><text x="161" y="315">6</text>
        </g>
      </svg>
      <svg class="chart-bar" style="position:absolute;left:270px;top:160px" width="270" height="160" viewBox="0 0 270 160">
        <g stroke="#e2e2e2" stroke-width=".6">
          <line x1="40" y1="8" x2="260" y2="8"/><line x1="40" y1="27" x2="260" y2="27"/>
          <line x1="40" y1="46" x2="260" y2="46"/><line x1="40" y1="65" x2="260" y2="65"/>
          <line x1="40" y1="84" x2="260" y2="84"/><line x1="40" y1="103" x2="260" y2="103"/>
          <line x1="40" y1="122" x2="260" y2="122"/><line x1="40" y1="141" x2="260" y2="141"/>
        </g>
        <g font-size="5" fill="#555" text-anchor="end">
          <text x="35" y="10">$1 400,00</text><text x="35" y="29">$1 200,00</text>
          <text x="35" y="48">$1 000,00</text><text x="35" y="67">$800,00</text>
          <text x="35" y="86">$600,00</text><text x="35" y="105">$400,00</text>
          <text x="35" y="124">$200,00</text><text x="35" y="143">$0,00</text>
        </g>
        <g fill="#3a6fcc">
          <rect x="49" y="88" width="6" height="53"/>
          <rect x="73" y="125" width="6" height="16"/>
          <rect x="97" y="116" width="6" height="25"/>
          <rect x="121" y="75" width="6" height="66"/>
          <rect x="145" y="47" width="6" height="94"/>
          <rect x="169" y="25" width="6" height="116"/>
          <rect x="193" y="60" width="6" height="81"/>
          <rect x="217" y="84" width="6" height="57"/>
          <rect x="241" y="115" width="6" height="26"/>
        </g>
        <g font-size="5" fill="#555" text-anchor="middle">
          <text x="52" y="151">1</text><text x="76" y="151">2</text><text x="100" y="151">3</text>
          <text x="124" y="151">4</text><text x="148" y="151">5</text><text x="172" y="151">6</text>
          <text x="196" y="151">7</text><text x="220" y="151">8</text><text x="244" y="151">9</text>
        </g>
      </svg>
      <div class="footer" style="left:333px">TARN RIDGE ©2019</div>
      <div class="page-num" style="left:653px">6</div>
    </div>
  </div>

</div>
</body>
</html>
```